Hospital Digital Whiteboard UI/UX Redesign

We are looking to update the look and feel of our Digital Whiteboards.
There are 4 separate layouts: Patient TV, Patient Room Whiteboard, Digital Door Sign, and Unit Care Board.
We want to have a unified, modern look across the portfolio.

```html
<!DOCTYPE html>
<html lang="en">
<head>
<meta charset="utf-8">
<title>Clearwell Health – Digital Whiteboards</title>
<link rel="stylesheet" href="https://fonts.googleapis.com/css2?family=Montserrat:wght@400;500;600;700;800&display=swap">
<style>
:root{
  --page:#eeeeee;
  --ink:#2a2f36;
  --muted:#7b8794;
  --brand:#1f9bd7;
  --sky-1:#e4f3fd;
  --sky-2:#bfe3fa;
  --sky-3:#8ccdf3;
  --white:#ffffff;
  --green:#6cb33f;
  --green-dark:#1f7a3a;
  --orange:#f08a24;
  --orange-soft:#f5a142;
  --blue:#1e90e0;
  --blue-deep:#1f6fe0;
  --red:#d9342b;
  --redorange:#e24a2a;
  --yellow:#e3c03a;
  --teal:#3bb3a0;
  --navy:#2b4a6e;
  --purple:#7b3fa8;
  --lime:#22c022;
  --pulse:#f4e600;
}
*{box-sizing:border-box;margin:0;padding:0}
html,body{width:1200px;height:4970px;overflow:hidden}
body{background:var(--page);font-family:"Montserrat",sans-serif;color:var(--ink)}
.canvas{position:relative;width:1200px;height:4970px;overflow:hidden}
.screen{position:absolute;overflow:hidden;box-shadow:0 2px 8px rgba(0,0,0,.12)}
.sky{background:linear-gradient(160deg,var(--sky-1) 0%,var(--sky-2) 55%,var(--sky-3) 100%)}

/* brand */
.brand{display:flex;align-items:center;gap:6px;color:var(--brand);font-weight:500;white-space:nowrap}
.brand .dot{width:12px;height:12px;border-radius:50%;background:var(--brand)}

/* ---------- Patient TV ---------- */
.tv{left:60px;top:125px;width:1073px;height:602px}
.tv .welcome{position:absolute;left:68px;top:33px;font-size:19px;line-height:24px;color:#3a4450}
.tv .brand{position:absolute;left:487px;top:38px;font-size:21px}
.tv .stamp{position:absolute;right:70px;top:45px;text-align:right;font-size:16px;font-weight:500}
.tv .stamp small{display:flex;justify-content:flex-end;align-items:center;gap:6px;font-size:13px;margin-top:6px}
.tile{position:absolute;background:var(--white);border-radius:6px;display:flex;flex-direction:column;align-items:center;justify-content:center;gap:12px;font-size:19px;font-weight:500;color:#3a4450;box-shadow:0 2px 6px rgba(30,100,160,.08)}
.tile.big{top:148px;width:222px;height:145px}
.tile.small{top:330px;width:222px;height:78px;flex-direction:row}
.tile svg{width:44px;height:44px}
.tile.small svg{width:30px;height:30px}
.tile.video{background:linear-gradient(135deg,#5a9ad6,#2e6bb7);color:var(--white)}
.tv .tagline{position:absolute;left:68px;top:462px;font-size:30px;font-weight:600;color:#3a4450}

/* ---------- Patient room whiteboard ---------- */
.room{left:56px;top:776px;width:1082px;height:607px}
.room .bar{position:absolute;left:0;top:0;width:100%;height:44px;background:var(--white);display:flex;align-items:center;padding:0 40px;font-size:17px;font-weight:500}
.room .bar .avatar{width:26px;height:26px;border-radius:50%;background:var(--blue);color:#fff;font-size:14px;display:flex;align-items:center;justify-content:center;margin-right:10px}
.room .bar .brand{position:absolute;left:505px;font-size:20px}
.room .bar .rno{margin-left:auto}
.card{position:absolute;background:var(--white);border-radius:4px;overflow:hidden}
.card .head{height:34px;display:flex;align-items:center;justify-content:center;gap:8px;color:#fff;font-size:13px;font-weight:600}
.head.green{background:var(--green)}.head.orange{background:var(--orange-soft)}.head.blue{background:var(--blue)}
.goals{left:45px;top:69px;width:255px;height:249px}
.goals .sec{padding:14px 22px 0}
.goals h4{color:var(--green);font-size:13px;font-weight:600;margin-bottom:7px}
.goals li{list-style:none;font-size:11px;color:#5a6470;line-height:17px;display:flex;gap:6px;align-items:center}
.goals li::before{content:"";width:9px;height:9px;border:1.4px solid #8a94a0;border-radius:50%}
.goals hr{border:0;border-top:1px solid #e3e6ea;margin:10px 22px 0}
.amb{left:45px;top:337px;width:255px;height:170px}
.amb ul{padding:14px 22px 0 44px;position:relative}
.amb li{list-style:none;font-size:10px;color:#304a9a;line-height:13px;margin-bottom:10px;position:relative}
.amb li small{display:block;color:#9aa3ad}
.amb li::before{content:"";position:absolute;left:-20px;top:2px;width:9px;height:9px;border-radius:50%;background:#cfd5db}
.amb li.now::before{background:var(--orange)}
.teams{left:326px;top:69px;width:432px;height:444px}
.member{display:flex;align-items:center;height:81px;padding:0 36px 0 44px;border-bottom:1px solid #edf0f3}
.face{width:44px;height:44px;border-radius:50%;background:linear-gradient(135deg,#c9d6e3,#8fa7bf);flex:none}
.member .who{margin-left:20px;font-size:13px;font-weight:600;flex:1}
.member .who small{display:block;color:var(--blue);font-weight:500;font-size:11px}
.phone{display:flex;align-items:center;gap:6px;color:var(--blue);font-size:12px;font-weight:500}
.discharge{left:777px;top:73px;width:256px;height:104px}
.discharge .val{display:flex;align-items:center;justify-content:center;gap:12px;height:70px;color:var(--green);font-size:27px;font-weight:500}
.dose{left:777px;top:197px;width:256px;height:170px}
.dose .row{display:flex;align-items:center;height:62px;padding:0 20px;gap:14px}
.pills{width:72px;height:36px;border-radius:18px;background:linear-gradient(90deg,#b9c1b4,#e0e3de)}
.dose .med{font-size:12px;color:#5a6470;text-align:center;flex:1}
.dose .med b{display:block;color:var(--orange);font-size:19px;font-weight:500}
.family{left:777px;top:386px;width:256px;height:127px}
.family .row{display:flex;justify-content:space-between;padding:10px 14px 0 12px;font-size:11px}
.family .row small{display:block;font-size:8px;color:var(--muted)}
.foot{position:absolute;left:0;bottom:0;width:100%;background:var(--white);display:flex;align-items:center;font-size:12px;color:#56606a;gap:8px}
.foot .links{margin-left:auto;display:flex;gap:24px;font-weight:500;color:#2f3a46}
.foot .links span{display:flex;align-items:center;gap:5px}
.room .foot{height:59px;padding:0 52px}

/* ---------- Unit care boards ---------- */
.unit{background:var(--white)}
.unit .top{display:flex;align-items:center;border-bottom:1px solid #e4e7ea;position:relative}
.unit .title{position:absolute;left:0;right:0;text-align:center;font-weight:500;color:#2f3a46}
.unit .clock{margin-left:auto;display:flex;align-items:center;gap:8px;color:#4a5560}
.grid{display:grid;align-items:center}
.colhead{font-weight:600;color:#2f3a46}
.row-line{border-bottom:1px solid #e6e9ec}
.st{display:flex;align-items:center;gap:5px}
.st::before{content:"";border-radius:50%;background:currentColor}
.st.vac{color:#4a5560}.st.doc{color:var(--blue)}.st.ok{color:var(--green)}.st.no{color:var(--red)}
.pill{border-radius:999px;color:#fff;text-align:center;font-weight:500}
.pill.cb{background:var(--blue-deep)}.pill.se{background:var(--redorange)}.pill.wa{background:#3a6fc4}
.pill.po{background:var(--pulse);color:#c86a00}.pill.pa{background:var(--orange-soft);color:#5a2e00}.pill.rn{background:var(--lime)}
.tags{display:flex;flex-wrap:wrap}
.tag{border-radius:50%;color:#fff;font-weight:700;font-style:normal;display:flex;align-items:center;justify-content:center;flex:none}
.cp{background:var(--red)}.fr{background:var(--yellow)}.wc{background:#2e8b3c}.np{background:var(--teal)}.ns{background:var(--teal)}.en{background:var(--green-dark)}.eo{background:var(--orange)}.ve{background:var(--navy)}

.board{left:60px;top:1437px;width:1080px;height:608px}
.board .top{height:87px;padding:0 40px 0 22px}
.board .brand{font-size:22px}
.board .title{font-size:34px}
.board .clock{font-size:23px}
.board .grid{grid-template-columns:56px 85px 89px 89px 125px 185px 197px 1fr;padding-left:23px;font-size:15px}
.board .colhead{height:52px;font-size:14px;padding-top:20px}
.board .colhead .c{text-align:center}
.board .r{height:76px}
.board .st::before{width:6px;height:6px}
.board .pill{width:174px;height:44px;line-height:44px;font-size:15px}
.board .pill.half{height:26px;line-height:26px;margin:2px 0}
.board .tags{gap:5px;padding-left:9px}
.board .tag{width:40px;height:40px;font-size:14px}

.tall{left:274px;top:2105px;width:606px;height:1078px;display:flex;flex-direction:column}
.tall .top{height:42px;padding:0 30px 0 16px;flex:none}
.tall .brand{font-size:12px}.tall .brand .dot{width:7px;height:7px}
.tall .title{font-size:19px}
.tall .clock{font-size:13px}
.tall .body{flex:1;display:flex;flex-direction:column;padding:0 14px 16px}
.tall .grid{grid-template-columns:34px 46px 44px 54px 70px 104px 120px 1fr;padding-left:10px;font-size:8px}
.tall .colhead{height:26px;font-size:7.5px;padding-top:8px}
.tall .colhead .c{text-align:center}
.tall .r{flex:1}
.tall .r.x{flex:1.5}
.tall .st::before{width:3px;height:3px}
.tall .pill{width:96px;height:18px;line-height:18px;font-size:7.5px}
.tall .pill.half{height:12px;line-height:12px;margin:1px 0}
.tall .tags{gap:3px;padding-left:8px;width:90px}
.tall .tag{width:18px;height:18px;font-size:7px}

/* ---------- Door signs ---------- */
.door .badges{position:absolute;left:33px;display:flex;flex-direction:column;gap:11px}
.badge{width:81px;height:66px;border-radius:6px;color:#fff;display:flex;flex-direction:column;align-items:center;justify-content:center;font-size:21px;font-weight:700;line-height:1}
.badge small{font-size:9px;font-weight:500;margin-top:5px}
.b-cp,.b-dp{background:var(--red)}.b-la{background:var(--orange)}.b-fr{background:var(--yellow)}.b-en{background:var(--green-dark)}.b-ns{background:var(--teal)}.b-ve{background:var(--navy)}
.door .brand{position:absolute;font-size:18px}
.roomcard{position:absolute;background:var(--white);border-radius:4px;text-align:center;color:var(--green);opacity:.95}
.roomcard span{display:block;font-size:18px;font-weight:500;padding-top:16px}
.roomcard b{display:block;font-size:70px;font-weight:700;line-height:74px}
.door .foot{height:33px;padding:0 38px;font-size:9.5px}
.door .foot .links{gap:18px;font-size:9.5px}

.door1{left:100px;top:3320px;width:504px;height:722px}
.door1 .badges{top:60px}
.door1 .brand{right:40px;top:22px}
.door1 .roomcard{left:149px;top:68px;width:314px;height:127px}
.visitor{position:absolute;left:149px;top:220px;width:314px;height:152px;background:var(--green);color:#fff;font-size:36px;font-weight:800;text-align:center;display:flex;align-items:center;justify-content:center;line-height:44px;border-radius:3px}
.visit{position:absolute;left:149px;top:389px;width:314px;height:119px;background:var(--white);border-radius:3px;overflow:hidden}
.visit .head{height:38px;background:#3b82e6;color:#fff;display:flex;align-items:center;justify-content:center;font-size:12px;font-weight:600}
.visit .who{display:flex;align-items:center;gap:16px;padding:14px 36px;font-size:13px;font-weight:500}
.visit .who .face{width:50px;height:50px}
.visit .meta{display:flex;gap:16px;font-size:9px;color:#5a6470;margin-top:6px}
.req{position:absolute;left:149px;width:314px;border-radius:3px;padding:10px 24px;display:flex;justify-content:space-between;font-size:20px;font-weight:700}
.req small{display:block;font-size:8px;font-weight:500;color:#5a6470}
.req i{font-style:normal;font-size:9px;font-weight:500;align-self:flex-end}
.req.water{top:527px;height:64px;background:var(--white);color:var(--green)}
.req.bed{top:604px;height:56px;background:var(--purple);color:#fff;align-items:center}
.req.bed i{align-self:center}

.door2{left:639px;top:3426px;width:501px;height:718px}
.door2 .badges{top:58px}
.door2 .brand{right:38px;top:18px}
.door2 .roomcard{left:151px;top:69px;width:310px;height:122px}
.codeblue{position:absolute;left:151px;top:216px;width:310px;height:442px;background:linear-gradient(180deg,#5aa2ee,#3d86e4);color:#fff;text-align:center;box-shadow:0 0 16px rgba(60,130,230,.5)}
.codeblue h2{font-size:55px;font-weight:800;line-height:64px;margin-top:122px}
.codeblue .time{font-size:34px;font-weight:500;margin-top:56px;display:flex;justify-content:center;align-items:center;gap:6px}
.codeblue p{font-size:26px;font-weight:500}

.door3{left:100px;top:4163px;width:492px;height:654px}
.door3 .brand{left:160px;top:24px}
.door3 .roomcard{left:42px;top:68px;width:402px;height:133px}
.quote{position:absolute;left:42px;top:259px;width:402px;height:301px;background:var(--white);border-radius:4px;text-align:center;color:var(--blue)}
.quote .mark{font-size:44px;font-weight:800;line-height:40px;margin-top:38px}
.quote q{display:block;font-size:34px;font-weight:500;line-height:47px;margin-top:6px}
.quote cite{display:block;font-style:normal;color:#2f3a46;font-size:22px;font-weight:500;margin-top:8px}
</style>
</head>
<body>
<div class="canvas">

<!-- Patient TV -->
<section class="screen sky tv">
  <div class="welcome">Welcome to<br><b style="font-weight:500">Clearwell Health</b></div>
  <div class="brand"><span class="dot"></span>Clearwell Health</div>
  <div class="stamp">Monday, February 23, 2023
    <small><svg width="16" height="16" viewBox="0 0 16 16"><circle cx="8" cy="8" r="6.5" fill="none" stroke="#2a2f36" stroke-width="1.5"/><path d="M8 4v4l3 2" stroke="#2a2f36" stroke-width="1.5" fill="none"/></svg>11:14 AM</small>
  </div>

  <div class="tile big video" style="left:68px" role="img" aria-label="Welcome video thumbnail showing a nurse">
    <svg viewBox="0 0 44 44" style="width:36px;height:36px"><circle cx="22" cy="22" r="19" fill="none" stroke="#fff" stroke-width="2.5"/><path d="M18 14l12 8-12 8z" fill="#fff"/></svg>
    <span>Welcome Video</span>
  </div>
  <div class="tile big" style="left:306px">
    <svg viewBox="0 0 44 44"><path d="M22 38 C6 27 4 18 8 12 C12 6 19 7 22 12 C25 7 32 6 36 12 C40 18 38 27 22 38Z" fill="#3a86e8"/><path d="M22 16v12M16 22h12" stroke="#fff" stroke-width="3"/></svg>
    <span>My Care</span>
  </div>
  <div class="tile big" style="left:545px">
    <svg viewBox="0 0 44 44"><path d="M4 10 C12 8 18 9 21 12 V38 C18 35 12 34 4 36Z M40 10 C32 8 26 9 23 12 V38 C26 35 32 34 40 36Z" fill="#3a86e8"/></svg>
    <span>Education</span>
  </div>
  <div class="tile big" style="left:783px">
    <svg viewBox="0 0 44 44"><rect x="6" y="6" width="32" height="24" rx="2" fill="none" stroke="#3a86e8" stroke-width="2.5"/><path d="M12 14h10M12 20h16M28 12l4 4" stroke="#3a86e8" stroke-width="2.5"/><path d="M16 36h12M22 30v6" stroke="#3a86e8" stroke-width="2.5"/></svg>
    <span>RX Search</span>
  </div>

  <div class="tile small" style="left:68px"><svg viewBox="0 0 30 30"><rect x="3" y="6" width="24" height="15" rx="1.5" fill="#3a86e8"/><path d="M10 25h10" stroke="#3a86e8" stroke-width="2.5"/></svg><span>Watch TV</span></div>
  <div class="tile small" style="left:306px"><svg viewBox="0 0 30 30"><rect x="4" y="7" width="22" height="16" rx="1.5" fill="#3a86e8"/><path d="M13 11l6 4-6 4z" fill="#fff"/></svg><span>Movies</span></div>
  <div class="tile small" style="left:545px"><svg viewBox="0 0 30 30"><circle cx="15" cy="6" r="3.5" fill="#3a86e8"/><path d="M15 10v7M6 14l9 3 9-3M5 24l10-7 10 7" stroke="#3a86e8" stroke-width="2.5" fill="none"/></svg><span>Relax</span></div>
  <div class="tile small" style="left:783px"><svg viewBox="0 0 30 30"><circle cx="14" cy="14" r="11" fill="#3a86e8"/><path d="M12 8v10a3 3 0 1 1-2-2.8V8h6v3h-4" fill="#fff"/></svg><span>Audio</span></div>

  <div class="tagline">Making each day better.™</div>
</section>

<!-- Patient Room Whiteboard -->
<section class="screen sky room">
  <div class="bar"><span class="avatar">A</span>Parker, Dana<div class="brand"><span class="dot"></span>Clearwell Health</div><span class="rno">Room 5131</span></div>

  <div class="card goals">
    <div class="head green">◎ Goals</div>
    <div class="sec"><h4>▭ Today's Goals</h4><ul><li>Walk 25 Feets</li></ul></div>
    <hr>
    <div class="sec"><h4>▭ Discharge Goals</h4><ul><li>Complete comprehension test</li><li>Review medications</li><li>Explain test result</li><li>Schedule follow-up</li></ul></div>
  </div>

  <div class="card amb">
    <div class="head orange">▣ Ambulation's status</div>
    <ul>
      <li class="now">Moving with support inside room<small>10/2/18</small></li>
      <li>Walking around in hall w/crutches<small>Goal 10/8/18</small></li>
      <li>Can walk around hall with no help<small>Goal 10/8/18</small></li>
    </ul>
  </div>

  <div class="card teams">
    <div class="head blue">▤ Care Teams</div>
    <div class="member"><div class="face" role="img" aria-label="Nurse manager portrait"></div><div class="who"><small>Nurse Manager</small>Leah Moreno, R.N</div><div class="phone">☏ 555-310-4820</div></div>
    <div class="member"><div class="face" role="img" aria-label="Charge nurse portrait"></div><div class="who"><small>Charge Nurse</small>Nina Carter</div><div class="phone">☏ 555-310-4820</div></div>
    <div class="member"><div class="face" role="img" aria-label="Duty nurse portrait"></div><div class="who"><small>Duty Nurse</small>Tessa Boyd</div><div class="phone">☏ 555-310-4820</div></div>
    <div class="member"><div class="face" role="img" aria-label="Patient care tech portrait"></div><div class="who"><small>Patient Care Tech</small>Omar Haddad</div><div class="phone">☏ 555-310-4820</div></div>
    <div class="member" style="border:0"><div class="face" role="img" aria-label="Social worker portrait"></div><div class="who"><small>Social Worker</small>Paul Whitman</div><div class="phone">☏ 555-310-4820</div></div>
  </div>

  <div class="card discharge">
    <div class="head green">▭ Anticipated day of discharge</div>
    <div class="val"><svg width="24" height="24" viewBox="0 0 24 24"><rect x="2" y="4" width="20" height="18" rx="2" fill="none" stroke="#6cb33f" stroke-width="2"/><path d="M2 9h20M7 2v4M17 2v4M6 13h3M11 13h3M16 13h2M6 17h3M11 17h3" stroke="#6cb33f" stroke-width="2"/></svg>11/10/2018</div>
  </div>

  <div class="card dose">
    <div class="head orange">▣ Next Dose</div>
    <div class="row"><div class="pills" role="img" aria-label="Oxycodone tablets"></div><div class="med">Oxycodone 5mg<b>11:00AM</b></div></div>
    <div class="row"><div class="pills" style="background:linear-gradient(90deg,#d9dcdf,#f2f3f4)" role="img" aria-label="Oxycodone tablets"></div><div class="med">Oxycodone 5mg<b>11:00AM</b></div></div>
  </div>

  <div class="card family">
    <div class="head blue">☏ Family contact</div>
    <div class="row"><div>Ethan Parker<small>Dad</small></div><div class="phone" style="font-size:11px">☏ 555-218-6034</div></div>
    <div class="row"><div>Grace Parker<small>Sister</small></div><div class="phone" style="font-size:11px">☏ 555-218-6034</div></div>
  </div>

  <div class="foot">Thursday,october 25th, 2022 &nbsp; ◷ 11:14 AM<div class="links"><span style="color:var(--green)">⚲ <b style="color:#2f3a46;font-weight:500">Floor Map</b></span><span style="color:var(--blue)">◎ <b style="color:#2f3a46;font-weight:500">Admin</b></span></div></div>
</section>

<!-- Unit Care Board (landscape) -->
<section class="screen unit board">
  <div class="top"><div class="brand"><span class="dot"></span>Clearwell Health</div><div class="title">Unit 2 West</div><div class="clock"><svg width="30" height="30" viewBox="0 0 30 30"><circle cx="15" cy="15" r="12" fill="none" stroke="#4a5560" stroke-width="2.5"/><path d="M15 8v8l5 3" stroke="#4a5560" stroke-width="2.5" fill="none"/></svg>11:14 AM</div></div>
  <div class="grid colhead"><span>RM #</span><span>PATIENT</span><span>NURSE</span><span>AIDE</span><span>ROUNDS</span><span class="c">STATUS</span><span class="c">ALERT</span><span class="c">INFOFILES</span></div>
  <div class="grid r row-line"><span>201</span><span>JT</span><span>Morgan</span><span>Delacroix</span><span>1:30 PM</span><span class="st doc">Doctor in Room</span><span class="pill cb">CODE BLUE 00:53</span><div class="tags"><i class="tag cp">CP</i><i class="tag cp">CP</i><i class="tag fr">FR</i><i class="tag wc">WC</i></div></div>
  <div class="grid r row-line"><span>201</span><span>JT</span><span>Morgan</span><span>Delacroix</span><span>1:30 PM</span><span class="st vac">Vacant</span><span></span><div class="tags"><i class="tag np">NP</i><i class="tag ns">NS</i></div></div>
  <div class="grid r row-line"><span>201</span><span>JT</span><span>Morgan</span><span>Delacroix</span><span>1:30 PM</span><span class="st doc">Staff in Room</span><span class="pill se">STAFF EMER 00:35</span><div class="tags"><i class="tag fr">FR</i></div></div>
  <div class="grid r row-line"><span>201</span><span>JT</span><span>Morgan</span><span>Delacroix</span><span>1:30 PM</span><span class="st vac">Vacant</span><span class="pill wa">WATER 00:35</span><div class="tags"><i class="tag np">NP</i><i class="tag en">EN</i></div></div>
  <div class="grid r row-line"><span>201</span><span>JT</span><span>Morgan</span><span>Delacroix</span><span>1:30 PM</span><span class="st ok">Visitor OK</span><span class="pill se">STAFF EMER 00:35</span><div class="tags"><i class="tag fr">FR</i></div></div>
  <div class="grid r"><span>201</span><span>JT</span><span>Morgan</span><span>Delacroix</span><span>1:30 PM</span><span class="st vac">Vacant</span><span><span class="pill po half" style="display:block">PULSE OX 00:35</span><span class="pill pa half" style="display:block">PAIN 00:35</span></span><div class="tags"><i class="tag np">NP</i><i class="tag eo">EN</i></div></div>
</section>

<!-- Unit Care Board (portrait) -->
<section class="screen unit tall">
  <div class="top"><div class="brand"><span class="dot"></span>Clearwell Health</div><div class="title">Unit 2 West</div><div class="clock">◷ 11:14 AM</div></div>
  <div class="body">
    <div class="grid colhead"><span>RM #</span><span>PATIENT</span><span>NURSE</span><span>AIDE</span><span>ROUNDS</span><span class="c">STATUS</span><span class="c">ALERT</span><span class="c">INFOFILES</span></div>
    <div class="grid r row-line"><span>201</span><span>JT</span><span>Morgan</span><span>Delacroix</span><span>1:30 PM</span><span class="st doc">Doctor in Room</span><span class="pill cb">CODE BLUE 00:53</span><div class="tags"><i class="tag cp">CP</i><i class="tag cp">CP</i><i class="tag fr">FR</i><i class="tag wc">WC</i></div></div>
    <div class="grid r row-line"><span>201</span><span>JT</span><span>Morgan</span><span>Delacroix</span><span>1:30 PM</span><span class="st vac">Vacant</span><span></span><div class="tags"><i class="tag np">NP</i><i class="tag ns">NS</i></div></div>
    <div class="grid r row-line"><span>201</span><span>JT</span><span>Morgan</span><span>Delacroix</span><span>1:30 PM</span><span class="st doc">Staff in Room</span><span class="pill se">STAFF EMER 00:35</span><div class="tags"><i class="tag fr">FR</i></div></div>
    <div class="grid r row-line"><span>201</span><span>JT</span><span>Morgan</span><span>Delacroix</span><span>1:30 PM</span><span class="st vac">Vacant</span><span class="pill wa">WATER 00:35</span><div class="tags"><i class="tag np">NP</i><i class="tag en">EN</i></div></div>
    <div class="grid r row-line"><span>201</span><span>JT</span><span>Morgan</span><span>Delacroix</span><span>1:30 PM</span><span class="st ok">Visitor OK</span><span class="pill se">STAFF EMER 00:35</span><div class="tags"><i class="tag fr">FR</i></div></div>
    <div class="grid r row-line"><span>201</span><span>JT</span><span>Morgan</span><span>Delacroix</span><span>1:30 PM</span><span class="st vac">Vacant</span><span><span class="pill po half" style="display:block">PULSE OX 00:35</span><span class="pill pa half" style="display:block">PAIN 00:35</span></span><div class="tags"><i class="tag np">NP</i><i class="tag eo">EN</i></div></div>
    <div class="grid r row-line"><span>201</span><span>JT</span><span>Morgan</span><span>Delacroix</span><span></span><span class="st ok">Visitor OK</span><span class="pill rn">RN NEED 00:35</span><div class="tags"><i class="tag fr">FR</i></div></div>
    <div class="grid r row-line"><span>201</span><span>JT</span><span>Morgan</span><span>Delacroix</span><span>1:30 PM</span><span class="st vac">Vacant</span><span></span><div class="tags"><i class="tag np">NP</i><i class="tag eo">EN</i></div></div>
    <div class="grid r row-line"><span>201</span><span>JT</span><span>Morgan</span><span>Delacroix</span><span></span><span class="st no">NO Visitor</span><span class="pill rn">RN NEED 00:35</span><div class="tags"><i class="tag fr">FR</i></div></div>
    <div class="grid r x row-line"><span>201</span><span>JT</span><span>Morgan</span><span>Delacroix</span><span>1:30 PM</span><span class="st vac">Vacant</span><span></span><div class="tags"><i class="tag cp">NP</i><i class="tag eo">EN</i><i class="tag cp">NP</i><i class="tag ve">VE</i><i class="tag cp">NP</i><i class="tag eo">EN</i><i class="tag cp">NP</i><i class="tag eo">EN</i></div></div>
    <div class="grid r row-line"><span>201</span><span>JT</span><span>Morgan</span><span>Delacroix</span><span>1:30 PM</span><span class="st doc">Doctor in Room</span><span class="pill cb">CODE BLUE 00:53</span><div class="tags"><i class="tag cp">CP</i><i class="tag cp">CP</i><i class="tag fr">FR</i><i class="tag wc">WC</i></div></div>
    <div class="grid r row-line"><span>201</span><span>JT</span><span>Morgan</span><span>Delacroix</span><span>1:30 PM</span><span class="st vac">Vacant</span><span><span class="pill po half" style="display:block">PULSE OX 00:35</span><span class="pill half" style="display:block;color:#2a2f36">PAIN 00:35</span></span><div class="tags"><i class="tag np">NP</i><i class="tag eo">EN</i></div></div>
    <div class="grid r row-line"><span>201</span><span>JT</span><span>Morgan</span><span>Delacroix</span><span></span><span class="st ok">Visitor OK</span><span class="pill rn">RN NEED 00:35</span><div class="tags"><i class="tag fr">FR</i></div></div>
    <div class="grid r row-line"><span>201</span><span>JT</span><span>Morgan</span><span>Delacroix</span><span>1:30 PM</span><span class="st vac">Vacant</span><span></span><div class="tags"><i class="tag np">NP</i><i class="tag eo">EN</i></div></div>
    <div class="grid r row-line"><span>201</span><span>JT</span><span>Morgan</span><span>Delacroix</span><span></span><span class="st no">NO Visitor</span><span class="pill rn">RN NEED 00:35</span><div class="tags"><i class="tag fr">FR</i></div></div>
    <div class="grid r x row-line"><span>201</span><span>JT</span><span>Morgan</span><span>Delacroix</span><span>1:30 PM</span><span class="st vac">Vacant</span><span></span><div class="tags"><i class="tag cp">NP</i><i class="tag eo">EN</i><i class="tag cp">NP</i><i class="tag fr">FR</i><i class="tag cp">NP</i><i class="tag eo">EN</i><i class="tag cp">NP</i><i class="tag eo">EN</i></div></div>
    <div class="grid r row-line"><span>201</span><span>JT</span><span>Morgan</span><span>Delacroix</span><span>1:30 PM</span><span class="st doc">Doctor in Room</span><span class="pill cb">CODE BLUE 00:53</span><div class="tags"><i class="tag cp">CP</i><i class="tag cp">CP</i><i class="tag fr">FR</i><i class="tag wc">WC</i></div></div>
    <div class="grid r row-line"><span>201</span><span>JT</span><span>Morgan</span><span>Delacroix</span><span>1:30 PM</span><span class="st vac">Vacant</span><span><span class="pill po half" style="display:block">PULSE OX 00:35</span><span class="pill half" style="display:block;color:#2a2f36">PAIN 00:35</span></span><div class="tags"><i class="tag np">NP</i><i class="tag eo">EN</i></div></div>
    <div class="grid r row-line"><span>201</span><span>JT</span><span>Morgan</span><span>Delacroix</span><span></span><span class="st no">NO Visitor</span><span class="pill rn">RN NEED 00:35</span><div class="tags"><i class="tag fr">FR</i></div></div>
    <div class="grid r row-line"><span>201</span><span>JT</span><span>Morgan</span><span>Delacroix</span><span>1:30 PM</span><span class="st vac">Vacant</span><span></span><div class="tags"><i class="tag np">NP</i><i class="tag eo">EN</i></div></div>
    <div class="grid r"><span>201</span><span>JT</span><span>Morgan</span><span>Delacroix</span><span></span><span class="st no">NO Visitor</span><span class="pill rn">RN NEED 00:35</span><div class="tags"><i class="tag fr">FR</i></div></div>
  </div>
</section>

<!-- Door Sign: visitor welcome -->
<section class="screen sky door door1">
  <div class="badges">
    <div class="badge b-cp">CP<small>Contact</small></div><div class="badge b-dp">DP<small>Contact</small></div><div class="badge b-la">LA<small>Contact</small></div><div class="badge b-fr">FR<small>Contact</small></div><div class="badge b-en">EN<small>Contact</small></div><div class="badge b-ns">NS<small>Contact</small></div><div class="badge b-ns">NS<small>Contact</small></div><div class="badge b-ve">VE<small>Contact</small></div>
  </div>
  <div class="brand"><span class="dot"></span>Clearwell Health</div>
  <div class="roomcard"><span>Room</span><b>216</b></div>
  <div class="visitor">VISITOR<br>WELCOME</div>
  <div class="visit">
    <div class="head">Last Staff Visit</div>
    <div class="who"><div class="face" role="img" aria-label="Nurse portrait"></div><div>Leah Moreno, R.N<div class="meta"><span>▭ 6/01/2023</span><span>◷ 1:58 AM</span></div></div></div>
  </div>
  <div class="req water"><div>WATER<small>Nurser Call</small></div><i>◷ 1:59 AM</i></div>
  <div class="req bed"><div>BED HEIGHT</div><i>◷ 1:59 AM</i></div>
  <div class="foot">Thursday,october 25th, 2022 &nbsp; ◷ 11:14 AM<div class="links"><span>⚲ Floor Map</span><span>◎ Admin</span></div></div>
</section>

<!-- Door Sign: code blue -->
<section class="screen sky door door2">
  <div class="badges">
    <div class="badge b-cp">CP<small>Contact</small></div><div class="badge b-dp">DP<small>Contact</small></div><div class="badge b-la">LA<small>Contact</small></div><div class="badge b-fr">FR<small>Contact</small></div><div class="badge b-en">EN<small>Contact</small></div><div class="badge b-ns">NS<small>Contact</small></div><div class="badge b-ns">NS<small>Contact</small></div><div class="badge b-ve">VE<small>Contact</small></div>
  </div>
  <div class="brand"><span class="dot"></span>Clearwell Health</div>
  <div class="roomcard"><span>Room</span><b>216</b></div>
  <div class="codeblue">
    <h2>CODE<br>BLUE</h2>
    <div class="time"><svg width="24" height="30" viewBox="0 0 24 30"><path d="M3 2h18M3 28h18M5 2c0 9 14 9 14 13S5 19 5 28M19 2c0 9-14 9-14 13s14 4 14 13" stroke="#fff" stroke-width="2.5" fill="none"/></svg>02:24</div>
    <p>Elapse Time</p>
  </div>
  <div class="foot">Thursday,october 25th, 2022 &nbsp; ◷ 11:14 AM<div class="links"><span>⚲ Floor Map</span><span>◎ Admin</span></div></div>
</section>

<!-- Door Sign: quote -->
<section class="screen sky door door3">
  <div class="brand"><span class="dot"></span>Clearwell Health</div>
  <div class="roomcard"><span>Room</span><b>216</b></div>
  <div class="quote">
    <div class="mark">”</div>
    <q>Believe you can and you’re halfway there.</q>
    <cite>— Eleanor Whitby</cite>
  </div>
  <div class="foot">Thursday,october 25th, 2022 &nbsp; ◷ 11:14 AM<div class="links"><span>⚲ Floor Map</span><span>◎ Admin</span></div></div>
</section>

</div>
</body>
</html>
```